Email Signatures

I would like to create a new email signature for my team. The design will be the same for everyone, with only individual details such as name and email changing. You can also see our brand style on our website. https://www.tlmbespokehomes.com.au/

Target Market(s)

Clients for new builds or renovations

Industry/Entity Type

Construction

Colors

Designer to choose colors to be used in the design.

```html
<!DOCTYPE html>
<html lang="en">
<head>
<meta charset="utf-8">
<title>TLM Bespoke Homes – Email Signature</title>
<link href="https://fonts.googleapis.com/css2?family=Playfair+Display:ital,wght@1,700&family=Roboto:wght@400;700&display=swap" rel="stylesheet">
<style>
  :root {
    --board: #dadada;
    --card-light: #f2f2f2;
    --card-dark: #1c1c1c;
    --green: #1a9645;
    --black: #000000;
    --white: #ffffff;
    --ink: #111111;
    --title-ink: #1e1e1e;
  }
  html, body {
    margin: 0;
    padding: 0;
    width: 1200px;
    height: 977px;
    overflow: hidden;
    background: var(--board);
  }
  .board {
    position: relative;
    width: 1200px;
    height: 977px;
    font-family: "Roboto", Arial, sans-serif;
  }
  .variant-title {
    position: absolute;
    left: 0;
    width: 1200px;
    text-align: center;
    margin: 0;
    font-family: "Playfair Display", Georgia, serif;
    font-style: italic;
    font-weight: 700;
    font-size: 38px;
    letter-spacing: 1px;
    color: var(--title-ink);
    text-shadow: 0 3px 4px rgba(0,0,0,.35);
  }
  .variant-title.top { top: 56px; }
  .variant-title.bottom { top: 880px; left: 40px; }

  .signature {
    position: absolute;
    left: 111px;
    width: 979px;
    height: 327px;
    box-shadow: 0 12px 16px rgba(0,0,0,.45);
    overflow: hidden;
  }
  .signature.light { top: 128px; background: var(--card-light); color: var(--ink); }
  .signature.dark { top: 517px; background: var(--card-dark); color: var(--white); }

  .signature .pattern-field {
    position: absolute;
    inset: 0;
  }
  .signature.light .pattern-field { background: var(--card-light); }
  .signature.dark .pattern-field { background: linear-gradient(180deg, #1f1f1f, #1a1a1a); }

  .accent-top {
    position: absolute;
    left: 0; top: 0;
    width: 20px; height: 80px;
  }
  .light .accent-top { background: var(--black); }
  .dark .accent-top { background: var(--white); }
  .accent-bar {
    position: absolute;
    left: 0; top: 82px; bottom: 0;
    width: 20px;
    background: var(--green);
  }

  .person-name {
    position: absolute;
    left: 51px; top: 4px;
    margin: 0;
    font-weight: 700;
    font-size: 42px;
    line-height: 48px;
    color: var(--green);
  }
  .person-role {
    position: absolute;
    left: 51px; top: 45px;
    margin: 0;
    font-weight: 400;
    font-size: 19px;
    line-height: 24px;
    letter-spacing: .5px;
  }

  .contact-list {
    position: absolute;
    left: 51px; top: 227px;
    margin: 0; padding: 0;
    list-style: none;
  }
  .contact-list li {
    display: flex;
    align-items: center;
    height: 26px;
    font-size: 20px;
    letter-spacing: .5px;
  }
  .contact-list svg {
    width: 17px; height: 17px;
    margin-right: 11px;
    flex: none;
  }

  .company-name {
    position: absolute;
    left: 690px; top: 128px;
    width: 240px;
    display: flex;
    align-items: center;
    gap: 12px;
    font-weight: 700;
  }
  .company-name .mark-square {
    width: 16px; height: 16px;
    background: var(--green);
    flex: none;
  }
  .company-name .name-text {
    display: block;
    line-height: 1;
  }
  .company-name .name-main { display: block; font-size: 80px; letter-spacing: 4px; }
  .company-name .name-sub { display: block; font-size: 16px; letter-spacing: 3.5px; margin-top: 12px; white-space: nowrap; }
  .light .company-name { color: var(--black); }
  .dark .company-name { color: var(--white); }
</style>
</head>
<body>
<main class="board">
  <h2 class="variant-title top">White Version</h2>

  <section class="signature light">
    <div class="pattern-field" role="img" aria-label="Faint repeating brand pattern across the signature background"></div>
    <div class="accent-top"></div>
    <div class="accent-bar"></div>
    <h1 class="person-name">Liam Harcourt</h1>
    <p class="person-role">General Manager</p>
    <ul class="contact-list">
      <li>
        <svg viewBox="0 0 24 24" aria-hidden="true"><path fill="#1a9645" d="M6.6 10.8a15 15 0 0 0 6.6 6.6l2.2-2.2a1 1 0 0 1 1-.25 11.4 11.4 0 0 0 3.6.6 1 1 0 0 1 1 1V20a1 1 0 0 1-1 1A17 17 0 0 1 3 4a1 1 0 0 1 1-1h3.5a1 1 0 0 1 1 1c0 1.25.2 2.45.6 3.6a1 1 0 0 1-.25 1z"/></svg>
        0412 555 018
      </li>
      <li>
        <svg viewBox="0 0 24 24" aria-hidden="true"><circle cx="12" cy="12" r="10" fill="none" stroke="#1a9645" stroke-width="2"/><path fill="none" stroke="#1a9645" stroke-width="1.6" d="M2 12h20M12 2c3 3 3 17 0 20M12 2c-3 3-3 17 0 20"/></svg>
        www.tlmbespokehomes.com.au
      </li>
      <li>
        <svg viewBox="0 0 24 24" aria-hidden="true"><rect x="2" y="6" width="20" height="14" fill="none" stroke="#1a9645" stroke-width="2"/><path fill="none" stroke="#1a9645" stroke-width="2" d="M2 6l10 8 10-8"/></svg>
        info@tlmbespokehomes.com.au
      </li>
    </ul>
    <div class="company-name">
      <span class="mark-square"></span>
      <span class="name-text"><span class="name-main">TLM</span><span class="name-sub">BESPOKE HOMES</span></span>
    </div>
  </section>

  <section class="signature dark">
    <div class="pattern-field" role="img" aria-label="Embossed repeating brand pattern across the dark signature background"></div>
    <div class="accent-top"></div>
    <div class="accent-bar"></div>
    <h1 class="person-name">Liam Harcourt</h1>
    <p class="person-role">General Manager</p>
    <ul class="contact-list">
      <li>
        <svg viewBox="0 0 24 24" aria-hidden="true"><path fill="#1a9645" d="M6.6 10.8a15 15 0 0 0 6.6 6.6l2.2-2.2a1 1 0 0 1 1-.25 11.4 11.4 0 0 0 3.6.6 1 1 0 0 1 1 1V20a1 1 0 0 1-1 1A17 17 0 0 1 3 4a1 1 0 0 1 1-1h3.5a1 1 0 0 1 1 1c0 1.25.2 2.45.6 3.6a1 1 0 0 1-.25 1z"/></svg>
        0412 555 018
      </li>
      <li>
        <svg viewBox="0 0 24 24" aria-hidden="true"><circle cx="12" cy="12" r="10" fill="none" stroke="#1a9645" stroke-width="2"/><path fill="none" stroke="#1a9645" stroke-width="1.6" d="M2 12h20M12 2c3 3 3 17 0 20M12 2c-3 3-3 17 0 20"/></svg>
        www.tlmbespokehomes.com.au
      </li>
      <li>
        <svg viewBox="0 0 24 24" aria-hidden="true"><rect x="2" y="6" width="20" height="14" fill="none" stroke="#1a9645" stroke-width="2"/><path fill="none" stroke="#1a9645" stroke-width="2" d="M2 6l10 8 10-8"/></svg>
        info@tlmbespokehomes.com.au
      </li>
    </ul>
    <div class="company-name">
      <span class="mark-square"></span>
      <span class="name-text"><span class="name-main">TLM</span><span class="name-sub">BESPOKE HOMES</span></span>
    </div>
  </section>

  <h2 class="variant-title bottom">Embossed Version</h2>
</main>
</body>
</html>
```